swimming pool Leak Detection Brochure

I would Like to create a pool leak detection brochure

Target Market(s)

High end Clients with inground swimming pools

Industry/Entity Type

Pool Service

Font styles to use
Other font styles liked:
• Im open to suggestions but using my website for ideas is suggested

Colors

Designer to choose colors to be used in the design.

Requirements
Must have
• Do you Have a Leak??
• Figuring out when your pool has a leak can be tough. Environmental factors do play a role in the water level, and just because your pool’s water is lower than normal does not mean it has a leak. Wind, humidity, and sun exposure all impact your rate of evaporation.
• Warning Signs of a Leak in Your Pool
• Your pool, fountain, or spa loses more than 1/4 an inch of water a day
• There are cracks in or around the pool decking
• You need to add water more than once a week
• Grass around the area is soggy
• Your pool deck is sinking or lifting
Nice to have
• PREPARING FOR A LEAK TEST
• To ensure you receive an accurate leak detection test, it is required that you have the pool vacuumed and cleaned beforehand. Dirt and debris in the pool can make it difficult to spot even large leaks. Likewise, the water should be as clear as possible. If your water is green it means mildew, algae, or fungi has infested it. Not only does this make it impossible to test for leaks, but it’s dangerous for our health. Finally our pool should be full to the normal level - we can’t find a leak that is not leaking! After your test, you will be confident knowing you have a pool/fountain/spa that is free of leaks or the Leak has been found and can be repaired Properly.

```html
<!DOCTYPE html>
<html lang="en">
<head>
<meta charset="utf-8">
<title>Harbor Tide Pool Service – Leak Detection Brochure</title>
<link href="https://fonts.googleapis.com/css2?family=Open+Sans:wght@400;600;700;800&family=Permanent+Marker&family=Noto+Serif&display=swap" rel="stylesheet">
<style>
:root{
  --stage:#2b2b2d;
  --blue-deep:#1a4fa3;
  --blue:#2470c9;
  --blue-bright:#2f9be0;
  --orange:#e8651f;
  --orange-dark:#d2531a;
  --paper:#f2f3f5;
  --paper-white:#fbfbfb;
  --ink:#2a2a2a;
  --ink-soft:#555;
  --white:#fff;
}
*{box-sizing:border-box;margin:0;padding:0}
html,body{width:1200px;height:880px;overflow:hidden;background:var(--stage)}
body{position:relative;font-family:"Open Sans",Arial,sans-serif;color:var(--ink)}
.spread{position:absolute;width:547px;height:394px;overflow:hidden;box-shadow:0 4px 14px rgba(0,0,0,.5)}
.spread-cover{left:34px;top:33px}
.spread-leak{left:619px;top:33px}
.spread-renovation{left:34px;top:460px}
.spread-services{left:619px;top:463px}
.panel{position:absolute;top:0;width:274px;height:394px}
.panel-left{left:0;background:var(--paper)}
.panel-right{left:274px;background:var(--paper-white)}
.abs{position:absolute}
.waves{position:absolute;left:0;top:0;width:547px;height:394px}
.photo{position:absolute;border-radius:50%;border:3px solid var(--white);box-shadow:0 0 0 1.5px var(--blue-bright);background:linear-gradient(160deg,#7fc7ea,#2a7fbf 60%,#1d5a8f)}
.photo.deck{background:linear-gradient(160deg,#c9bba4,#8f8270 70%,#5f564a)}
.photo.gear{background:linear-gradient(160deg,#e6e6e6,#9a9a9a 70%,#3b3b3b)}
.photo.cover{background:linear-gradient(160deg,#6ea9c7,#3e6f86 60%,#2f4a55)}
.photo.garden{background:linear-gradient(160deg,#8fbf6a,#3f8fc0 60%,#2b5f8f)}
.brush{font-family:"Permanent Marker",cursive;font-weight:400;letter-spacing:.5px;line-height:1.2}
.brush .accent{color:var(--blue-bright)}
.brush-blue{color:var(--blue-bright)}
.head-orange{font-weight:700;color:var(--orange);font-size:9.5px;letter-spacing:.1px}
.head-orange.caps{text-transform:uppercase}
.rule{position:absolute;height:1px;background:var(--blue-bright)}
.fine{font-size:3.9px;line-height:1.45;color:var(--ink-soft);text-align:justify}
.small{font-size:5.2px;line-height:1.45;color:var(--ink-soft);text-align:justify}
.ticks{list-style:none}
.ticks li{position:relative;padding-left:9px;font-size:5.6px;font-weight:700;color:var(--ink);line-height:1.9}
.ticks li::before{content:"";position:absolute;left:0;top:2.4px;width:4px;height:2px;border-left:1.2px solid var(--orange);border-bottom:1.2px solid var(--orange);transform:rotate(-45deg)}
.ticks.light li{font-weight:400;color:var(--ink-soft);font-size:5px;line-height:2.1}
.ticks .feature{font-size:7.6px;color:var(--orange);text-transform:uppercase;line-height:1.5;margin-bottom:3px}
.ticks .feature::before{top:3.4px}
.web{font-size:8px;color:var(--white)}
.web b{font-weight:700}
.globe{display:inline-block;width:6px;height:6px;border:1px solid var(--white);border-radius:50%;margin-right:3px;vertical-align:-0.5px}
.cover-left{background:linear-gradient(180deg,#2e6fc4,#1b4e9e)}
.testimonial{position:absolute;left:110px;width:150px;color:var(--white);font-size:4.2px;line-height:1.5;text-align:right}
.testimonial .stars{color:var(--orange);font-size:8px;letter-spacing:1px;display:block;margin-bottom:3px}
.testimonial .who{font-weight:700;font-size:6.8px;display:block;margin-top:5px}
.quote-mark{position:absolute;font-family:"Noto Serif",serif;font-size:30px;color:rgba(255,255,255,.55);line-height:1}
.badge{position:absolute;border-radius:50%;background:var(--white);border:3px solid #9ec6ee}
.badge::after{content:"";position:absolute;inset:6px;border-radius:50%;background:#cfe0f3}
.contact-title{font-weight:700;color:var(--white);font-size:8.6px}
.contact-lines{color:var(--white);font-size:6.6px;line-height:1.75}
.member-box{position:absolute;background:var(--white);border-bottom:7px solid var(--blue-deep)}
.phone-pill{position:absolute;border:1.2px solid var(--white);border-radius:12px;color:var(--white);font-weight:800;font-size:13px;display:flex;align-items:center;gap:6px;padding-left:4px}
.phone-icon{width:14px;height:14px;border:1.2px solid var(--white);border-radius:50%;display:flex;align-items:center;justify-content:center}
.cover-photo{position:absolute;left:274px;top:0;width:273px;height:300px;background:linear-gradient(180deg,#5aa7e6 0%,#9fd0f0 22%,#3f9a5a 32%,#38b3d9 48%,#1f7fc4 80%)}
.logo-circle{position:absolute;border-radius:50%;background:var(--white);border:4px solid #3a8fd8;box-shadow:0 0 0 2px var(--white);display:flex;flex-direction:column;align-items:center;justify-content:center;text-align:center}
.logo-circle span{font-weight:700;color:var(--blue-deep);font-size:9.5px;line-height:1.2}
.tagline{font-family:"Noto Serif",serif;color:var(--white);font-size:16.5px;line-height:1.35}
.brand-tile{position:absolute;background:#dfe4ec;border-radius:2px}
.phone-line{color:var(--white);font-weight:800;font-size:13.5px;display:flex;align-items:center;gap:6px}
.blue-note{color:var(--blue-bright);font-weight:700;font-size:6.6px;line-height:1.5}
.sub-strong{font-weight:700;font-size:9px;color:var(--ink)}
.sub-strong small{font-weight:400;font-size:7px}
.leak-logo{position:absolute;border-radius:50%;background:var(--white);border:3px solid var(--white);box-shadow:0 0 0 1.5px var(--blue-bright);display:flex;align-items:center;justify-content:center}
.leak-logo::after{content:"";width:60%;height:60%;border-radius:50%;background:#d9d9d9}
</style>
</head>
<body>

<section class="spread spread-cover">
  <div class="panel panel-left cover-left">
    <div class="abs" role="img" aria-label="Pool cleaning net skimming clear blue water" style="left:0;top:0;width:118px;height:160px;background:linear-gradient(150deg,#6fb3e8,#3b82cf 60%,rgba(46,111,196,0))"></div>
    <span class="quote-mark" style="left:148px;top:30px">“</span>
    <p class="testimonial" style="top:40px"><span class="stars">★★★★★</span>I am so happy I found this company. All service! I highly recommend this company, my pool was green all last summer with another company. This pool service came in and within 3 days my pool turned around. We are beyond happy.<span class="who">Corinne L.</span></p>
    <span class="quote-mark" style="left:250px;top:100px">”</span>
    <span class="quote-mark" style="left:118px;top:112px">“</span>
    <p class="testimonial" style="top:118px"><span class="stars">★★★★★</span>I was a longtime customer of a bigger company in the area and needed my pool opened on short notice. The other company didn't return my calls, and when I got ahold of them they quoted me 6 weeks. I found this crew in online reviews and decided to take a chance.<span class="who">Tomas R.</span></p>
    <span class="quote-mark" style="left:250px;top:176px">”</span>
  </div>
  <div class="cover-photo" role="img" aria-label="Luxury resort swimming pool with swimmers, palm trees and blue sky"></div>
  <svg class="waves" viewBox="0 0 547 394" preserveAspectRatio="none" aria-hidden="true">
    <path d="M0 240 C80 205 190 215 274 260 C360 300 440 270 547 210 L547 394 L0 394Z" fill="#1f5fb8"/>
    <path d="M0 240 C80 205 190 215 274 260 C360 300 440 270 547 210" fill="none" stroke="#ffffff" stroke-width="3"/>
    <path d="M0 252 C90 220 190 230 274 272 C360 312 440 282 547 222" fill="none" stroke="#5bb0ef" stroke-width="1.2"/>
    <path d="M274 300 C360 330 450 310 547 280 L547 394 L274 394Z" fill="#1b55a8" opacity=".6"/>
  </svg>
  <div class="badge" style="left:24px;top:207px;width:46px;height:46px"></div>
  <div class="badge" style="left:88px;top:196px;width:44px;height:44px"></div>
  <div class="badge" style="left:154px;top:190px;width:44px;height:44px"></div>
  <div class="badge" style="left:209px;top:208px;width:38px;height:38px"></div>
  <p class="contact-title abs" style="left:112px;top:255px">CONTACT US</p>
  <p class="contact-lines abs" style="left:112px;top:272px">Harbor Tide Pool Service<br>RI REG # 40817<br>CT License # SP1-PLM 0519306<br>✉ info@harbortidepools.com</p>
  <div class="member-box" style="left:27px;top:326px;width:64px;height:40px"></div>
  <div class="phone-pill" style="left:112px;top:334px;width:138px;height:20px"><span class="phone-icon"><svg width="8" height="8" viewBox="0 0 24 24"><path d="M6.6 10.8a15 15 0 0 0 6.6 6.6l2.2-2.2c.3-.3.7-.4 1-.2 1.1.4 2.3.6 3.6.6.6 0 1 .4 1 1V20c0 .6-.4 1-1 1A17 17 0 0 1 3 4c0-.6.4-1 1-1h3.5c.6 0 1 .4 1 1 0 1.3.2 2.5.6 3.6.1.3 0 .7-.2 1z" fill="#fff"/></svg></span>401-555-0142</div>
  <p class="web abs" style="left:112px;top:365px"><span class="globe"></span>www.<b>harbortidepools</b>.com</p>
  <div class="logo-circle" style="left:412px;top:194px;width:98px;height:98px"><span>Harbor Tide<br>Pool Service</span></div>
  <p class="tagline abs" style="left:303px;top:315px">Dive Into<br>Professional Pool<br>Service &amp; Repair</p>
  <p class="web abs" style="left:446px;top:370px">www.<b>harbortidepools</b>.com</p>
</section>

<section class="spread spread-leak">
  <div class="panel panel-left"></div>
  <div class="panel panel-right"></div>
  <svg class="waves" viewBox="0 0 547 394" preserveAspectRatio="none" aria-hidden="true">
    <path d="M0 340 C100 335 190 320 274 290 L274 394 L0 394Z" fill="var(--orange)"/>
    <path d="M0 334 C100 329 190 314 274 284" fill="none" stroke="#fff" stroke-width="4"/>
    <path d="M0 328 C100 323 190 308 274 278" fill="none" stroke="#2f9be0" stroke-width="1"/>
    <path d="M274 355 C390 350 470 330 547 298 L547 394 L274 394Z" fill="var(--orange)"/>
    <path d="M274 349 C390 344 470 324 547 292" fill="none" stroke="#fff" stroke-width="4"/>
    <path d="M274 343 C390 338 470 318 547 286" fill="none" stroke="#2f9be0" stroke-width="1"/>
    <path d="M274 394 L274 0" stroke="#dcdcdc" stroke-width=".6"/>
  </svg>
  <h2 class="brush abs" style="left:29px;top:20px;font-size:13px">DO YOU HAVE A <span class="accent">LEAK??</span></h2>
  <div class="rule" style="left:0;top:40px;width:250px"></div>
  <ul class="ticks light abs" style="left:29px;top:46px;width:214px">
    <li><span class="small" style="display:block;font-size:5px;line-height:1.4;padding-top:1px">Figuring out when your pool has a leak can be tough. Environmental factors do play a role in the water level, and just because your pool's water is lower than normal does not mean it has a leak. Wind, humidity, and sun exposure all impact your rate of evaporation.</span></li>
    <li>Warning Signs of a Leak in Your Pool</li>
    <li>Your pool, fountain, or spa loses more than 1/4 an inch of water a day</li>
    <li>There are cracks in or around the pool decking</li>
    <li>You need to add water more than once a week</li>
    <li>Grass around the area is soggy</li>
    <li>Your pool deck is sinking or lifting</li>
  </ul>
  <h2 class="brush abs" style="left:29px;top:149px;font-size:13px">PREPARING FOR A <span class="accent">LEAK TEST?</span></h2>
  <div class="rule" style="left:0;top:169px;width:250px"></div>
  <p class="small abs" style="left:29px;top:175px;width:214px;font-size:4.9px">To ensure you receive an accurate leak detection test, it is required that you have the pool vacuumed and cleaned beforehand. Dirt and debris in the pool can make it difficult to spot even large leaks. Likewise, the water should be as clear as possible. If your water is green it means mildew, algae, or fungi has infested it. Not only does this make it impossible to test for leaks, but it's dangerous for our health. Finally our pool should be full to the normal level - we can't find a leak that is not leaking! After your test, you will be confident knowing you have a pool/fountain/spa that is free of leaks or the Leak has been found and can be repaired Properly.</p>
  <div class="brand-tile" style="left:29px;top:258px;width:24px;height:16px"></div>
  <div class="brand-tile" style="left:57px;top:260px;width:24px;height:14px"></div>
  <div class="brand-tile" style="left:89px;top:260px;width:68px;height:12px"></div>
  <div class="brand-tile" style="left:29px;top:280px;width:60px;height:9px"></div>
  <div class="brand-tile" style="left:99px;top:280px;width:48px;height:10px"></div>
  <div class="brand-tile" style="left:49px;top:293px;width:40px;height:8px"></div>
  <div class="brand-tile" style="left:105px;top:292px;width:36px;height:12px"></div>
  <div class="photo gear" role="img" aria-label="Leak detection equipment kit in open case" style="left:155px;top:266px;width:106px;height:106px"></div>
  <p class="phone-line abs" style="left:31px;top:363px"><span class="phone-icon"><svg width="8" height="8" viewBox="0 0 24 24"><path d="M6.6 10.8a15 15 0 0 0 6.6 6.6l2.2-2.2c.3-.3.7-.4 1-.2 1.1.4 2.3.6 3.6.6.6 0 1 .4 1 1V20c0 .6-.4 1-1 1A17 17 0 0 1 3 4c0-.6.4-1 1-1h3.5c.6 0 1 .4 1 1 0 1.3.2 2.5.6 3.6.1.3 0 .7-.2 1z" fill="#fff"/></svg></span>401-555-0142</p>

  <h2 class="brush brush-blue abs" style="left:302px;top:24px;font-size:13.5px;line-height:1.55">POOL MAINTENANCE,<br>CLEANING, &amp; REPAIRS IN RI</h2>
  <p class="sub-strong abs" style="left:302px;top:73px">HARBOR TIDE POOL SERVICE <small>RI, MA, CT</small></p>
  <div class="rule" style="left:296px;top:88px;width:251px"></div>
  <p class="small abs" style="left:302px;top:93px;width:217px;font-size:4.9px">Serving Massachusetts, Rhode Island, including Block Island and Connecticut, Harbor Tide Pool Service stands ready to provide exceptional pool maintenance for the swimming pool at your home or on your commercial property. Whether it's a high-end vacation resort, hotel, apartment complex or a private residence, we can provide pool cleaning, repair and maintenance of pools anywhere in RI.</p>
  <p class="sub-strong abs" style="left:302px;top:148px">Benefits of Harbor Tide Pool Service</p>
  <div class="rule" style="left:296px;top:163px;width:251px"></div>
  <p class="small abs" style="left:302px;top:168px;width:217px;font-size:4.9px">As a family owned and operated small business the founder, Evan Delcourt, is sure to spend extra time with each customer to better serve them. While the "big boys" may have more representatives, they are always ready to move on to the next transaction.</p>
  <p class="small abs" style="left:302px;top:199px;width:217px;font-size:4.9px">We have always strived to provide a high level of pool service at the initial stages of a transaction as well as after the job is complete. We want you to love your pool by having it cleaned and properly maintained on a regular basis.</p>
  <p class="blue-note abs" style="left:302px;top:235px">Your satisfaction is GUARANTEED.<br>For Pool Repair, Maintenance, and Cleaning<br>Call Harbor Tide Pool Service TODAY!!!!</p>
  <div class="photo" role="img" aria-label="Yellow rubber duck floating in an infinity pool" style="left:301px;top:275px;width:88px;height:88px"></div>
  <div class="photo" role="img" aria-label="Technician cleaning a rooftop pool" style="left:424px;top:259px;width:96px;height:96px"></div>
  <p class="web abs" style="left:433px;top:372px"><span class="globe"></span>www.<b>harbortidepools</b>.com</p>
</section>

<section class="spread spread-renovation">
  <div class="panel panel-left"></div>
  <div class="panel panel-right"></div>
  <svg class="waves" viewBox="0 0 547 394" preserveAspectRatio="none" aria-hidden="true">
    <path d="M0 345 C110 335 200 318 274 300 L274 394 L0 394Z" fill="var(--orange)"/>
    <path d="M0 339 C110 329 200 312 274 294" fill="none" stroke="#fff" stroke-width="4"/>
    <path d="M0 333 C110 323 200 306 274 288" fill="none" stroke="#2f9be0" stroke-width="1"/>
    <path d="M274 352 C390 345 470 328 547 305 L547 394 L274 394Z" fill="var(--orange)"/>
    <path d="M274 346 C390 339 470 322 547 299" fill="none" stroke="#fff" stroke-width="4"/>
    <path d="M274 340 C390 333 470 316 547 293" fill="none" stroke="#2f9be0" stroke-width="1"/>
  </svg>
  <h2 class="brush brush-blue abs" style="left:29px;top:20px;font-size:13px">RENOVATION</h2>
  <div class="rule" style="left:0;top:41px;width:260px"></div>
  <p class="fine abs" style="left:29px;top:46px;width:230px">Is your swimming pool beginning to age? Is the coping loose, is your tile cracked and falling off, and are your pavers crumbling? We blend old-time craftsmanship with modern technology to restore and redesign your backyard. We take the time to understand your goals and budget, then guide you through every choice so your pool looks and performs like new again.</p>
  <h3 class="head-orange caps abs" style="left:29px;top:104px">Pool Decking Removal and Renovation</h3>
  <div class="rule" style="left:0;top:118px;width:260px"></div>
  <p class="fine abs" style="left:29px;top:122px;width:230px">Demolition of existing pool decking is done with care using modern tools so the pool and surroundings stay protected. The surface is then prepared for new decking, and many material options are available to match your home.</p>
  <h3 class="head-orange caps abs" style="left:29px;top:154px">Types of Decking:</h3>
  <div class="rule" style="left:0;top:167px;width:150px"></div>
  <ul class="ticks abs" style="left:29px;top:172px">
    <li>Stamped Concrete</li><li>Pavers</li><li>Exposed Aggregate</li><li>Blue Stone</li><li>Plain Concrete</li>
  </ul>
  <div class="photo deck" role="img" aria-label="Paver pool deck under construction" style="left:172px;top:148px;width:52px;height:52px"></div>
  <div class="photo deck" role="img" aria-label="Demolished pool deck with exposed shell" style="left:134px;top:184px;width:56px;height:56px"></div>
  <div class="photo" role="img" aria-label="Finished pool with new concrete decking" style="left:196px;top:190px;width:46px;height:46px"></div>
  <h3 class="head-orange caps abs" style="left:29px;top:237px">Structural Repair</h3>
  <div class="rule" style="left:0;top:250px;width:120px"></div>
  <p class="fine abs" style="left:29px;top:254px;width:230px">We can repair sections of compromised pool walls and steps, and alter pool depth when needed. Cracks are injected and reinforced so the structure stays sound.</p>
  <ul class="ticks abs" style="left:29px;top:273px;width:150px;display:flex;flex-wrap:wrap;column-gap:10px">
    <li>Wall Repair</li><li>Step Replacement</li><li>Pool Depth Alterations</li><li>Inferior Walls</li><li>Crack Repair &amp; Injection</li>
  </ul>
  <div class="photo deck" role="img" aria-label="Pool shell with rebar during structural repair" style="left:98px;top:328px;width:50px;height:50px"></div>
  <div class="photo deck" role="img" aria-label="Excavated pool with wall forms" style="left:156px;top:304px;width:80px;height:80px"></div>
  <p class="web abs" style="left:29px;top:378px"><span class="globe"></span>www.<b>harbortidepools</b>.com</p>

  <h3 class="head-orange caps abs" style="left:300px;top:20px">Plumbing Updates and Upgrades</h3>
  <div class="rule" style="left:294px;top:33px;width:253px"></div>
  <p class="fine abs" style="left:300px;top:37px;width:225px">A leak in the return or suction lines can waste water and strain equipment. We replace skimmers, inlets and main drains, and bring all plumbing up to current code with new fittings sized for your system.</p>
  <ul class="ticks abs" style="left:300px;top:68px">
    <li>Inlets</li><li>Skimmer Replacements</li><li>Main Drain Replacement</li><li>Automatic Pool Cleaners</li>
  </ul>
  <h3 class="head-orange caps abs" style="left:300px;top:116px">Pool Coping Removal &amp; Replacement</h3>
  <div class="rule" style="left:294px;top:129px;width:253px"></div>
  <p class="fine abs" style="left:300px;top:133px;width:225px">Existing pool coping is removed, and the surface is prepared for new coping. There are many coping options to choose from to match your project design.</p>
  <p class="abs" style="left:300px;top:154px;font-size:5.4px;font-weight:700">TYPES OF POOL COPING:</p>
  <ul class="ticks abs" style="left:300px;top:161px">
    <li>Bullnose Brick</li><li>Cantilever</li><li>White Coping</li><li>Blue Stone</li><li>Cantilever Poured Band</li>
  </ul>
  <div class="photo" role="img" aria-label="Pool edge with new stone coping" style="left:394px;top:150px;width:54px;height:54px"></div>
  <div class="photo" role="img" aria-label="Waterline tile and coping detail" style="left:438px;top:152px;width:64px;height:64px"></div>
  <h3 class="head-orange caps abs" style="left:300px;top:224px">Tile Removal &amp; Replacement</h3>
  <div class="rule" style="left:294px;top:237px;width:253px"></div>
  <p class="fine abs" style="left:300px;top:241px;width:225px">Existing waterline tile is completely removed and the surface is prepared for new tile.</p>
  <ul class="ticks abs" style="left:300px;top:251px;width:230px">
    <li class="feature">Pool Interior Resurfacing / Replastering</li>
    <li class="feature">Filter System and Equipment<br>Upgrades / Replacement:</li>
  </ul>
  <div class="photo gear" role="img" aria-label="Pool pump and filter equipment pad" style="left:306px;top:318px;width:54px;height:54px"></div>
  <div class="photo gear" role="img" aria-label="New pool filter and heater installation" style="left:360px;top:300px;width:70px;height:70px"></div>
  <div class="photo" role="img" aria-label="Worker tiling a pool interior with blue mosaic" style="left:440px;top:290px;width:80px;height:80px"></div>
</section>

<section class="spread spread-services">
  <div class="panel panel-left"></div>
  <div class="panel panel-right"></div>
  <svg class="waves" viewBox="0 0 547 394" preserveAspectRatio="none" aria-hidden="true">
    <path d="M0 352 C110 345 200 330 274 315 L274 394 L0 394Z" fill="var(--orange)"/>
    <path d="M0 346 C110 339 200 324 274 309" fill="none" stroke="#fff" stroke-width="4"/>
    <path d="M0 340 C110 333 200 318 274 303" fill="none" stroke="#2f9be0" stroke-width="1"/>
    <path d="M274 355 C390 348 470 330 547 300 L547 394 L274 394Z" fill="var(--orange)"/>
    <path d="M274 349 C390 342 470 324 547 294" fill="none" stroke="#fff" stroke-width="4"/>
    <path d="M274 343 C390 336 470 318 547 288" fill="none" stroke="#2f9be0" stroke-width="1"/>
  </svg>
  <h2 class="brush brush-blue abs" style="left:29px;top:21px;font-size:12.5px;line-height:1.5">WEEKLY POOL SERVICES &amp;<br>MORE IN BLOCK ISLAND, RI</h2>
  <div class="rule" style="left:0;top:60px;width:260px"></div>
  <h3 class="head-orange abs" style="left:29px;top:64px">Pool Opening</h3>
  <div class="rule" style="left:0;top:78px;width:160px"></div>
  <p class="fine abs" style="left:29px;top:83px;width:135px">When we open your pool you can expect the cover to be cleaned, folded and removed, and the pool checked for damage.</p>
  <p class="fine abs" style="left:29px;top:102px;width:135px">Pool water is then shocked and walls brushed, equipment is started and tested, with any needed repairs noted.</p>
  <h3 class="head-orange abs" style="left:29px;top:128px">Pool Closing</h3>
  <div class="rule" style="left:0;top:142px;width:160px"></div>
  <p class="fine abs" style="left:29px;top:147px;width:135px">Lower water to proper level, blow out water from all plumbing lines and plug them, drain filter and heater, remove deck equipment, add winter chemicals, install cover.</p>
  <h3 class="head-orange abs" style="left:29px;top:179px">Equipment Repair and Upgrades</h3>
  <div class="rule" style="left:0;top:193px;width:160px"></div>
  <p class="fine abs" style="left:29px;top:198px;width:135px">We service all equipment as well as upgrade older equipment to more energy efficient products. Some of the brands we service include major pump, filter, heater and cleaner makers.</p>
  <h3 class="head-orange abs" style="left:29px;top:235px">Weekly Pool Service</h3>
  <div class="rule" style="left:0;top:249px;width:160px"></div>
  <p class="fine abs" style="left:29px;top:254px;width:135px">Weekly pool service includes chemical balancing, shocking, skimming and filter back washing, filter maintenance, adding water to the pool, cleaning and maintaining skimmer baskets, and a vacuum service. We travel throughout the island on a daily basis, so anything that arises can be handled in a timely manner.</p>
  <div class="photo garden" role="img" aria-label="Backyard pool being opened in spring" style="left:191px;top:71px;width:52px;height:52px"></div>
  <div class="photo cover" role="img" aria-label="Pool with winter safety cover" style="left:167px;top:113px;width:62px;height:62px"></div>
  <div class="photo" role="img" aria-label="Pool opened and filled for the season" style="left:201px;top:137px;width:64px;height:64px"></div>
  <div class="photo gear" role="img" aria-label="Pool heater and equipment pad" style="left:175px;top:191px;width:60px;height:60px"></div>
  <div class="photo garden" role="img" aria-label="Technician servicing a pool beside a house" style="left:199px;top:227px;width:60px;height:60px"></div>
  <div class="photo" role="img" aria-label="Robotic cleaner on the floor of a clear pool" style="left:145px;top:305px;width:86px;height:86px"></div>
  <p class="web abs" style="left:29px;top:376px"><span class="globe"></span>www.<b>harbortidepools</b>.com</p>

  <h3 class="head-orange abs" style="left:301px;top:20px">Safety Cover Repair or Replacement</h3>
  <div class="rule" style="left:294px;top:34px;width:253px"></div>
  <p class="fine abs" style="left:301px;top:40px;width:112px">Using quality covers we strive for customer safety by either replacing or repairing your winter cover.</p>
  <h3 class="head-orange abs" style="left:301px;top:68px">Renovation</h3>
  <div class="rule" style="left:294px;top:82px;width:140px"></div>
  <p class="fine abs" style="left:301px;top:87px;width:125px">Tile repair, coping repair or replacement, plaster or even pool painting, you name it we can do it.</p>
  <div class="photo cover" role="img" aria-label="Pool covered with a safety cover" style="left:417px;top:51px;width:52px;height:52px"></div>
  <div class="photo" role="img" aria-label="Renovated pool with new plaster" style="left:443px;top:83px;width:60px;height:60px"></div>
  <div class="photo" role="img" aria-label="Rectangular pool with stone deck" style="left:427px;top:117px;width:70px;height:70px"></div>
  <h2 class="brush brush-blue abs" style="left:301px;top:124px;font-size:11px;line-height:1.35">BLOCK ISLAND POOL<br>SERVICES</h2>
  <div class="rule" style="left:294px;top:157px;width:130px"></div>
  <ul class="ticks abs" style="left:301px;top:163px">
    <li>Block Island Pool Openings</li><li>Block Island Pool Closings</li><li>Block Island Weekly Pool Service</li>
  </ul>
  <p class="abs" style="left:301px;top:206px;font-size:6px;color:var(--ink)">Things Harbor Tide has Done To Make working on BI Easier and more Affordable:</p>
  <p class="fine abs" style="left:301px;top:217px;width:225px">We have staff on the island a minimum of three days a week from April through October. We have an island vehicle to make emergencies easier to manage, and we work with local builders on needed assistance.</p>
  <ul class="ticks abs" style="left:301px;top:253px">
    <li class="brush brush-blue" style="font-size:10px;line-height:1.8;font-weight:400;color:var(--blue-bright)">COMMERCIAL POOL SERVICES</li>
    <li class="brush brush-blue" style="font-size:10px;line-height:1.8;font-weight:400;color:var(--blue-bright)">POOL LEAK DETECTION</li>
  </ul>
  <div class="leak-logo" role="img" aria-label="Leak detection partner badge" style="left:308px;top:312px;width:50px;height:50px"></div>
  <div class="photo garden" role="img" aria-label="Lounge chair beside a pool" style="left:353px;top:292px;width:70px;height:70px"></div>
  <div class="photo" role="img" aria-label="Child sitting on the edge of a pool" style="left:429px;top:297px;width:80px;height:80px"></div>
</section>

</body>
</html>
```